Site for company producing and selling products for children's health

We need an appealing professional web site design and images for a brand new company producing and selling products focused on children’s health. The site will offer information to visitors on the company, the company’s products, and general resources related to children’s health. Additionally the site will offer e-commerce functionality to allow for ordering of the company’s products.
The content and navigation for the site will be generated by programming, such as php or asp, and therefore any images used in the navigation portions of the site should allow for HTML markup to be overlaid rather than having the text built into the image or graphic.
The design must include 2 layouts, one for the landing/home page that includes only top navigation, and an inner page layout that includes both top and left navigation.
The header area of the site should include a place for links to access the visitor’s cart and profile similar to the top sections of quillbarn.com, tervodo.com, and pikmart.com.
The landing page of the site should include some type of “changing” image area where we can include multiple image files for rotation to visitors similar to what is seen at vorlo.com or mallowkite.com. The flash/animation mechanism does not need to be provided (although it would be a plus if it was) but the design must accommodate the space for it.
The company’s colors are Orange (FF9900) and Blue (0066FF) and the logo can be viewed at http://corvanelkids.com/logo.png
All CSS and markup provided must be display consistently in Internet Explorer 7+, FifeFox, Google Chrome, and Safari.
Incorporating social media links (facebook, twitter, etc.) is desirable.
Target Market(s)
Parents who are conscious of health risks associated with children's diets and consumer food products.
Industry/Entity Type
E-Commerce
Look and feel
Each slider illustrates characteristics of the customer's brand and the style your logo design should communicate.

```html
<!DOCTYPE html>
<html lang="en">
<head>
<meta charset="utf-8">
<title>Corvanel Kids – Home</title>
<link href="https://fonts.googleapis.com/css2?family=Arimo:wght@400;700&family=Oswald:wght@500&display=swap" rel="stylesheet">
<style>
:root{
  --blue:#0066ff;
  --blue-deep:#1a55d8;
  --orange:#ff9900;
  --orange-deep:#e8650a;
  --ink:#1d1d1d;
  --panel:#eeeeee;
  --card:#c8c8c8;
  --card-dark:#23272a;
  --sky-light:#e4f0fb;
  --sky-mid:#a9cdee;
  --red:#e0181b;
  --foot-top:#77839f;
  --foot-bot:#4a5880;
}
*{margin:0;padding:0;box-sizing:border-box}
html,body{width:1053px;height:1200px;overflow:hidden;background:#fff}
body{font-family:"Arimo",Arial,sans-serif;color:var(--ink)}
.page{position:absolute;left:0;top:0;width:1002px;height:1142px;transform:scale(1.0509);transform-origin:0 0;
  background:linear-gradient(#fafafa,#f1f1f1 190px,#fff 190px)}
.abs{position:absolute}

/* top navigation */
.topbar{left:10px;top:0;width:983px;height:42px;border-radius:0 0 8px 8px;
  background:linear-gradient(#8fb8ff,#3d86ff 45%,var(--blue) 100%);box-shadow:0 3px 5px rgba(0,0,0,.35)}
.topnav{left:36px;top:13px;display:flex;gap:15px;font-size:11px;font-weight:700;color:#fff}
.btn-category{left:807px;top:9px;width:171px;height:22px;border:1px solid #6b3d00;border-radius:4px;
  background:linear-gradient(#ffc04d,var(--orange));font-size:11px;font-weight:700;color:#111;
  padding:5px 0 0 19px}
.arrow-box{display:inline-flex;width:13px;height:12px;background:#fff;border-radius:2px;position:absolute;right:11px;top:5px;align-items:center;justify-content:center}

/* header */
.brand-mark{left:54px;top:82px;display:flex;align-items:center;gap:8px;font-size:22px;font-weight:700;color:var(--blue)}
.brand-mark i{display:block;width:26px;height:26px;border-radius:50%;background:var(--orange)}
.site-title{left:385px;top:84px;font-size:56px;font-weight:700;color:var(--orange-deep);letter-spacing:.5px}

/* hero */
.hero{left:10px;top:187px;width:983px;height:343px;background:var(--panel);border-radius:6px 6px 0 0}
.hero-slide{left:26px;top:226px;width:548px;height:291px;
  background:linear-gradient(180deg,#8fbde8 0%,#b9d4e8 30%,#d9d2c4 48%,#c89a7a 66%,#e6a8b8 82%,#f0c9a8 100%)}
.welcome{left:600px;top:232px;font-size:22px;font-weight:700;color:#111}
.welcome span{font-size:30px;font-weight:400;color:var(--orange)}
.intro{left:600px;top:281px;width:368px;font-size:12px;line-height:17px;color:#222}
.intro p+p{margin-top:17px}
.btn-read{left:601px;top:483px;width:134px;height:34px;background:var(--blue);color:#fff;font-size:16px;padding:7px 0 0 11px}

/* ticker */
.ticker{left:11px;top:544px;width:981px;height:57px;border:1px solid #86a9c8;
  background:linear-gradient(var(--sky-light),var(--sky-mid))}
.btn-pill{height:27px;border:1px solid #c46a00;border-radius:4px;background:linear-gradient(#ffc05a,var(--orange));
  font-size:12px;font-weight:700;color:#222;display:flex;align-items:center}
.btn-prev{left:20px;top:560px;width:89px;padding-left:28px}
.btn-next{left:509px;top:560px;width:89px;padding-left:31px}
.btn-pill .arrow-box{top:7px}
.btn-prev .arrow-box{left:8px;right:auto}
.ticker-text{left:116px;top:564px;font-size:15px;color:#0d2f78}
.follow{left:626px;top:557px;font-family:"Oswald",Arial,sans-serif;font-size:20px;color:var(--red)}
.social{width:26px;height:26px;border-radius:50%;top:559px;background:radial-gradient(circle at 40% 35%,#5d8fd6,#1a4a9a)}

/* side navigation */
.sidenav{left:10px;top:618px;width:260px;height:451px;background:var(--blue);padding:30px 16px 0 19px}
.sidenav li{list-style:none;height:30px;border-bottom:1px solid #4d94ff;display:flex;align-items:center;
  font-size:11px;font-weight:700;color:#fff}
.sidenav li svg{margin:0 13px 0 2px}

/* products */
.card{width:220px;height:199px;background:var(--card)}
.card-inner{position:absolute;left:9px;top:10px;width:201px;height:151px;background:var(--card-dark)}
.card-photo{position:absolute;left:14px;top:14px;width:122px;height:124px}
.card-tag{position:absolute;left:150px;top:14px;width:34px;height:124px;display:flex;align-items:center;justify-content:center}
.card-tag span{transform:rotate(-90deg);white-space:nowrap;color:#fff;font-size:17px;font-weight:700}
.card-name{position:absolute;left:32px;top:169px;font-size:16px;color:#111}
.btn-more{left:283px;top:1045px;width:128px;height:25px;background:#222;color:#fff;font-size:12px;font-weight:700;text-align:center;padding-top:6px}
.pager{left:425px;top:1050px;display:flex;align-items:center;gap:8px;font-size:11px;font-weight:700;color:#111}
.pager b{display:inline-block;width:2px;height:11px;background:#111}

/* footer */
.footer{left:11px;top:1083px;width:981px;height:59px;background:linear-gradient(var(--foot-top),var(--foot-bot));
  color:#fff;font-size:11px;text-align:center;padding-top:13px}
.footer nav{display:flex;justify-content:center;gap:15px;margin-bottom:5px}
</style>
</head>
<body>
<div class="page">

  <header>
    <div class="abs topbar"></div>
    <nav class="abs topnav"><span>Home</span><span>Latest News</span><span>About Us</span><span>Services</span><span>Product Page</span><span>Contact Us</span></nav>
    <div class="abs btn-category">SHOP BY CATEGORY
      <span class="arrow-box"><svg width="6" height="8" viewBox="0 0 6 8"><path d="M1 0l4 4-4 4" fill="none" stroke="#e08a00" stroke-width="2"/></svg></span></div>
    <div class="abs brand-mark"><i></i>Corvanel Kids</div>
    <h1 class="abs site-title">Corvanel Kids</h1>
  </header>

  <section>
    <div class="abs hero"></div>
    <div class="abs hero-slide" role="img" aria-label="Rotating banner photo: a family sharing a healthy outdoor meal in front of their house"></div>
    <h2 class="abs welcome">welcome to <span>Corvanel Kids</span></h2>
    <div class="abs intro">
      <p>Lorem Ipsum is simply dummy text of the printing and typesetting industry. Lorem Ipsum has been the industry's standard dummy text ever since the 1500s, when an unknown printer took a galley of type and scrambled it to make a type specimen book. It has survived not only five centuries, but also the leap into electronic typesetting, remaining essentially unchanged.</p>
      <p>It was popularised in the 1960s with the release of Pressline sheets containing Lorem Ipsum passages, and more recently with desktop publishing software like Fennic PageSetter including versions of Lorem Ipsum.</p>
    </div>
    <div class="abs btn-read">Read More
      <svg style="position:absolute;left:103px;top:12px" width="16" height="10" viewBox="0 0 16 10" fill="#fff"><rect x="0" y="0" width="3" height="3"/><rect x="0" y="7" width="3" height="3"/><rect x="4" y="3.5" width="3" height="3"/><rect x="9" y="0" width="3" height="3"/><rect x="9" y="7" width="3" height="3"/><rect x="13" y="3.5" width="3" height="3"/></svg></div>
  </section>

  <section>
    <div class="abs ticker"></div>
    <div class="abs btn-pill btn-prev"><span class="arrow-box"><svg width="6" height="8" viewBox="0 0 6 8"><path d="M5 0L1 4l4 4" fill="none" stroke="#e08a00" stroke-width="2"/></svg></span>Previous</div>
    <div class="abs ticker-text">Lorem ipsum dolo sit amet nuno valencia estat di morea</div>
    <div class="abs btn-pill btn-next">Next<span class="arrow-box"><svg width="6" height="8" viewBox="0 0 6 8"><path d="M1 0l4 4-4 4" fill="none" stroke="#e08a00" stroke-width="2"/></svg></span></div>
    <div class="abs follow">Follow us on</div>
    <div class="abs social" style="left:748px"></div>
    <div class="abs social" style="left:809px"></div>
    <div class="abs social" style="left:871px"></div>
  </section>

  <aside class="abs sidenav">
    <ul>
      <li><svg width="14" height="9" viewBox="0 0 14 9" fill="#fff"><rect x="0" y="0" width="3" height="3"/><rect x="0" y="6" width="3" height="3"/><rect x="4" y="3" width="3" height="3"/><rect x="7" y="0" width="3" height="3"/><rect x="7" y="6" width="3" height="3"/><rect x="11" y="3" width="3" height="3"/></svg>Lorem Ipsum dolor sit amet</li>
      <li><svg width="14" height="9" viewBox="0 0 14 9" fill="#fff"><rect x="0" y="0" width="3" height="3"/><rect x="0" y="6" width="3" height="3"/><rect x="4" y="3" width="3" height="3"/><rect x="7" y="0" width="3" height="3"/><rect x="7" y="6" width="3" height="3"/><rect x="11" y="3" width="3" height="3"/></svg>Lorem Ipsum dolor sit amet</li>
      <li><svg width="14" height="9" viewBox="0 0 14 9" fill="#fff"><rect x="0" y="0" width="3" height="3"/><rect x="0" y="6" width="3" height="3"/><rect x="4" y="3" width="3" height="3"/><rect x="7" y="0" width="3" height="3"/><rect x="7" y="6" width="3" height="3"/><rect x="11" y="3" width="3" height="3"/></svg>Lorem Ipsum dolor sit amet</li>
      <li><svg width="14" height="9" viewBox="0 0 14 9" fill="#fff"><rect x="0" y="0" width="3" height="3"/><rect x="0" y="6" width="3" height="3"/><rect x="4" y="3" width="3" height="3"/><rect x="7" y="0" width="3" height="3"/><rect x="7" y="6" width="3" height="3"/><rect x="11" y="3" width="3" height="3"/></svg>Lorem Ipsum dolor sit amet</li>
      <li><svg width="14" height="9" viewBox="0 0 14 9" fill="#fff"><rect x="0" y="0" width="3" height="3"/><rect x="0" y="6" width="3" height="3"/><rect x="4" y="3" width="3" height="3"/><rect x="7" y="0" width="3" height="3"/><rect x="7" y="6" width="3" height="3"/><rect x="11" y="3" width="3" height="3"/></svg>Lorem Ipsum dolor sit amet</li>
      <li><svg width="14" height="9" viewBox="0 0 14 9" fill="#fff"><rect x="0" y="0" width="3" height="3"/><rect x="0" y="6" width="3" height="3"/><rect x="4" y="3" width="3" height="3"/><rect x="7" y="0" width="3" height="3"/><rect x="7" y="6" width="3" height="3"/><rect x="11" y="3" width="3" height="3"/></svg>Lorem Ipsum dolor sit amet</li>
      <li><svg width="14" height="9" viewBox="0 0 14 9" fill="#fff"><rect x="0" y="0" width="3" height="3"/><rect x="0" y="6" width="3" height="3"/><rect x="4" y="3" width="3" height="3"/><rect x="7" y="0" width="3" height="3"/><rect x="7" y="6" width="3" height="3"/><rect x="11" y="3" width="3" height="3"/></svg>Lorem Ipsum dolor sit amet</li>
      <li><svg width="14" height="9" viewBox="0 0 14 9" fill="#fff"><rect x="0" y="0" width="3" height="3"/><rect x="0" y="6" width="3" height="3"/><rect x="4" y="3" width="3" height="3"/><rect x="7" y="0" width="3" height="3"/><rect x="7" y="6" width="3" height="3"/><rect x="11" y="3" width="3" height="3"/></svg>Lorem Ipsum dolor sit amet</li>
      <li><svg width="14" height="9" viewBox="0 0 14 9" fill="#fff"><rect x="0" y="0" width="3" height="3"/><rect x="0" y="6" width="3" height="3"/><rect x="4" y="3" width="3" height="3"/><rect x="7" y="0" width="3" height="3"/><rect x="7" y="6" width="3" height="3"/><rect x="11" y="3" width="3" height="3"/></svg>Lorem Ipsum dolor sit amet</li>
      <li><svg width="14" height="9" viewBox="0 0 14 9" fill="#fff"><rect x="0" y="0" width="3" height="3"/><rect x="0" y="6" width="3" height="3"/><rect x="4" y="3" width="3" height="3"/><rect x="7" y="0" width="3" height="3"/><rect x="7" y="6" width="3" height="3"/><rect x="11" y="3" width="3" height="3"/></svg>Lorem Ipsum dolor sit amet</li>
      <li><svg width="14" height="9" viewBox="0 0 14 9" fill="#fff"><rect x="0" y="0" width="3" height="3"/><rect x="0" y="6" width="3" height="3"/><rect x="4" y="3" width="3" height="3"/><rect x="7" y="0" width="3" height="3"/><rect x="7" y="6" width="3" height="3"/><rect x="11" y="3" width="3" height="3"/></svg>Lorem Ipsum dolor sit amet</li>
      <li><svg width="14" height="9" viewBox="0 0 14 9" fill="#fff"><rect x="0" y="0" width="3" height="3"/><rect x="0" y="6" width="3" height="3"/><rect x="4" y="3" width="3" height="3"/><rect x="7" y="0" width="3" height="3"/><rect x="7" y="6" width="3" height="3"/><rect x="11" y="3" width="3" height="3"/></svg>Lorem Ipsum dolor sit amet</li>
      <li><svg width="14" height="9" viewBox="0 0 14 9" fill="#fff"><rect x="0" y="0" width="3" height="3"/><rect x="0" y="6" width="3" height="3"/><rect x="4" y="3" width="3" height="3"/><rect x="7" y="0" width="3" height="3"/><rect x="7" y="6" width="3" height="3"/><rect x="11" y="3" width="3" height="3"/></svg>Lorem Ipsum dolor sit amet</li>
    </ul>
  </aside>

  <main>
    <div class="abs card" style="left:283px;top:618px"><div class="card-inner">
      <div class="card-photo" role="img" aria-label="Product photo: colourful jelly beans spilling from a jar" style="background:linear-gradient(135deg,#e0302a,#f4c21c 35%,#3aa53a 60%,#e86a1a 85%,#c8dde6)"></div>
      <div class="card-tag"><span>Product 1</span></div></div><div class="card-name">Product 1</div></div>
    <div class="abs card" style="left:515px;top:618px"><div class="card-inner">
      <div class="card-photo" role="img" aria-label="Product photo: slice of tomato pizza" style="background:radial-gradient(circle at 45% 50%,#e8a030,#d4541c 55%,#f2e0b0 80%,#fff)"></div>
      <div class="card-tag"><span>Product 2</span></div></div><div class="card-name">Product 2</div></div>
    <div class="abs card" style="left:747px;top:618px"><div class="card-inner">
      <div class="card-photo" role="img" aria-label="Product photo: plated appetiser with a carved carrot flower" style="background:linear-gradient(135deg,#f4efe6,#e8b27a 40%,#e4542a 60%,#f6f2ec)"></div>
      <div class="card-tag"><span>Product 3</span></div></div><div class="card-name">Product 3</div></div>
    <div class="abs card" style="left:283px;top:835px"><div class="card-inner">
      <div class="card-photo" role="img" aria-label="Product photo: grapes and a bottle on a wooden table" style="background:linear-gradient(160deg,#a07848,#6a3a2a 45%,#8a2030 65%,#c89058)"></div>
      <div class="card-tag"><span>Product 4</span></div></div><div class="card-name">Product 4</div></div>
    <div class="abs card" style="left:515px;top:835px"><div class="card-inner">
      <div class="card-photo" role="img" aria-label="Product photo: wrap sandwich with tomato and greens" style="background:linear-gradient(135deg,#fff,#d83a2a 20%,#d8b890 45%,#c89070 70%,#5a9a3a)"></div>
      <div class="card-tag"><span>Product 5</span></div></div><div class="card-name">Product 5</div></div>
    <div class="abs card" style="left:747px;top:835px"><div class="card-inner">
      <div class="card-photo" role="img" aria-label="Product photo: whole pizza with toppings" style="background:radial-gradient(circle,#c8602a,#a8401e 50%,#e8b060 68%,#fff 72%)"></div>
      <div class="card-tag"><span>Product 6</span></div></div><div class="card-name">Product 6</div></div>

    <div class="abs btn-more">See More Products</div>
    <div class="abs pager">
      <svg width="11" height="11" viewBox="0 0 11 11"><rect x=".5" y=".5" width="10" height="10" fill="#fff" stroke="#111"/><path d="M7 2.5L3.5 5.5 7 8.5z" fill="#111"/></svg>
      <span>1</span><b></b><span>2</span><b></b><span>3</span><b></b><span>4</span><b></b><span>5</span><b></b><span>6</span>
      <svg width="11" height="11" viewBox="0 0 11 11"><rect x=".5" y=".5" width="10" height="10" fill="#fff" stroke="#111"/><path d="M4 2.5l3.5 3L4 8.5z" fill="#111"/></svg>
    </div>
  </main>

  <footer class="abs footer">
    <nav><span>Home</span><span>Latest News</span><span>About Us</span><span>Services</span><span>Product Page</span><span>Contact Us</span></nav>
    <div>© Copyright &nbsp; | &nbsp; All Rights Reserved</div>
  </footer>

</div>
</body>
</html>
```